Sheriff Candidate needs a large yard sign

A candidate for Sheriff needs to have a sign to put in front of businesses and houses that advertise her candidacy.

Target Market(s)

Democrats, voters

Industry/Entity Type

Political

Font styles to use
Sans Serif

Colors
34a7d7
3276b5

Requirements
Must have
• Must have her picture
• Must have the words "Elect Dana Holloway" - I'd like the name Dana to be smaller Holloway. "Elect" and "Holloway" should be the focus.
• at the bottom in a box "Paid for by the Committee to Elect Dana Holloway"
Nice to have
• it would be good to have her logo as well.
• blue color for democrats and on a white background
Should not have
• pink color

```html
<!DOCTYPE html>
<html lang="en">
<head>
<meta charset="utf-8">
<title>Elect Dana Holloway – Yard Sign</title>
<link rel="stylesheet" href="https://fonts.googleapis.com/css2?family=Tinos:wght@400;700&family=Open+Sans:wght@400;600&display=swap">
<style>
  :root {
    --blue-deep: #3276b5;
    --blue-light: #34a7d7;
    --bg-top: #ffffff;
    --bg-bottom: #eef1f5;
    --gold: #c9a43a;
    --photo-dark: #1f2738;
    --photo-mid: #3b4352;
  }
  html, body {
    margin: 0;
    padding: 0;
    overflow: hidden;
    background: #ffffff;
  }
  .yard-sign {
    position: relative;
    width: 1200px;
    height: 751px;
    overflow: hidden;
    background: linear-gradient(160deg, var(--bg-top) 0%, #f6f8fa 55%, var(--bg-bottom) 100%);
  }
  .accent-band {
    position: absolute;
    inset: 0;
  }
  .headline-elect {
    position: absolute;
    left: 292px;
    top: 56px;
    margin: 0;
    font-family: "Tinos", "Times New Roman", serif;
    font-weight: 400;
    font-size: 160px;
    line-height: 1;
    color: var(--blue-deep);
    letter-spacing: -1px;
  }
  .headline-first-name {
    position: absolute;
    left: 80px;
    top: 362px;
    margin: 0;
    transform-origin: 0 0;
    transform: rotate(-90deg);
    font-family: "Tinos", "Times New Roman", serif;
    font-size: 58px;
    line-height: 1;
    color: var(--blue-light);
    letter-spacing: 1px;
  }
  .headline-last-name {
    position: absolute;
    left: 146px;
    top: 196px;
    margin: 0;
    font-family: "Tinos", "Times New Roman", serif;
    font-weight: 400;
    font-size: 152px;
    line-height: 1;
    color: var(--blue-deep);
    letter-spacing: -1px;
  }
  .campaign-mark {
    position: absolute;
    left: 330px;
    top: 406px;
    width: 232px;
    height: 232px;
    display: flex;
    align-items: center;
    justify-content: center;
  }
  .campaign-mark-circle {
    position: absolute;
    inset: 0;
    border-radius: 50%;
    background: var(--gold);
  }
  .campaign-mark-name {
    position: relative;
    width: 170px;
    text-align: center;
    font-family: "Tinos", "Times New Roman", serif;
    font-weight: 700;
    font-size: 26px;
    line-height: 1.15;
    color: #ffffff;
  }
  .paid-for {
    position: absolute;
    left: 163px;
    top: 692px;
    margin: 0;
    font-family: "Open Sans", Arial, sans-serif;
    font-size: 21px;
    letter-spacing: 0.4px;
    color: var(--blue-light);
  }
  .candidate-photo {
    position: absolute;
    left: 776px;
    top: 30px;
    width: 424px;
    height: 721px;
    border-radius: 170px 170px 0 0;
    background: linear-gradient(180deg, #b08a72 0%, #c79a80 30%, var(--photo-mid) 46%, var(--photo-dark) 100%);
  }
</style>
</head>
<body>
  <main class="yard-sign">
    <svg class="accent-band" width="1200" height="751" viewBox="0 0 1200 751" aria-hidden="true">
      <path d="M932 0 H1200 V700 C1150 520 1030 260 932 0 Z" fill="var(--blue-deep)"/>
    </svg>

    <h1 class="headline-elect">Elect</h1>
    <p class="headline-first-name">DANA</p>
    <p class="headline-last-name">Holloway</p>

    <div class="campaign-mark">
      <span class="campaign-mark-circle"></span>
      <span class="campaign-mark-name">Holloway for Sheriff</span>
    </div>

    <p class="paid-for">Paid for by the Committee to Elect Dana Holloway</p>

    <div class="candidate-photo" role="img" aria-label="Portrait photo of candidate Dana Holloway, smiling, wearing a navy blazer"></div>
  </main>
</body>
</html>
```